TWR Handyman Service

File 2 Prep kitchen cabinets
File 3 Painting kitchen cabinets
File 4 Demo stairs
File 5 Completion Installing stair treads
File 6 Power washing deck
File 7 Completion of Sainting deck and railings
File 8 Completion of staining steps
Logo, owner name, email and web site on front cover
File 9 Demo living room floor
File 10 Completion of living room floor
Please see additional on attached flyer

Target Market(s)

Residential

Industry/Entity Type

Painting

Font styles to use
Serif
Sans Serif

Requirements
Must have
• Some Photos and type of work discerption
Front page Logo, web address, phone number, owners name and email address
Back Page see attached file 1
Nice to have
• Photo maybe in middle of flyer
Use the best text that you think will meet the needs
Should not have
• No pink colors

```html
<!DOCTYPE html>
<html lang="en">
<head>
<meta charset="utf-8">
<title>TWR Handyman Services – Trifold Brochure</title>
<link href="https://fonts.googleapis.com/css2?family=Montserrat:wght@400;500;600;700;800&family=Roboto:wght@400;500&family=Roboto+Slab:wght@700&family=Yellowtail&display=swap" rel="stylesheet">
<style>
:root{
  --stage:#333335;
  --blue:#3d5ce0;
  --gold:#c9a66b;
  --ink:#1f1f22;
  --paper:#f3f3f3;
  --paper-2:#e9e9ea;
  --text:#2b2b2e;
  --white:#ffffff;
}
*{box-sizing:border-box;margin:0;padding:0}
html,body{width:1200px;height:2586px;overflow:hidden;background:var(--stage)}
body{position:relative;font-family:"Roboto",Arial,sans-serif;color:var(--text)}
.section-label{position:absolute;left:60px;font:400 24px "Montserrat",sans-serif;color:var(--white);letter-spacing:.5px}
.spread{position:absolute;left:60px;width:1080px;height:838px;background:linear-gradient(180deg,var(--paper),var(--paper-2));overflow:hidden}
.spread > *{position:absolute}
.spread-bg{left:0;top:0;width:1080px;height:838px}
.photo{border:3px solid var(--white);box-shadow:0 1px 3px rgba(0,0,0,.25)}
.bottom-bar{left:0;top:784px;width:1080px;height:54px;display:flex}
.bottom-bar div{flex:1;display:flex;align-items:center;justify-content:center;color:var(--white);font:500 14px "Roboto",sans-serif}
.bottom-bar .blue{background:var(--blue)}
.bottom-bar .gold{background:var(--gold);color:var(--ink)}
.bottom-bar .call{font-family:"Montserrat",sans-serif;font-weight:700;letter-spacing:.5px}
.ticks{list-style:none}
.ticks li{position:relative;padding-left:24px;font-size:14px;line-height:1.2}
.ticks li::before{content:"";position:absolute;left:0;top:2px;width:11px;height:11px;border:1.5px solid var(--blue);border-radius:50%}
.ticks li::after{content:"";position:absolute;left:4.5px;top:4.5px;width:3px;height:5px;border:solid var(--blue);border-width:0 1.5px 1.5px 0;transform:rotate(45deg)}
.brand{display:flex;align-items:center;gap:10px;font:700 17px "Roboto Slab",serif;color:var(--ink)}
.brand-square{border:4px solid var(--blue)}
/* outside */
.intro{left:26px;top:36px;width:310px;font-size:12.5px;line-height:1.35}
.action-grid{left:26px;top:120px;width:310px;display:grid;grid-template-columns:1fr 1fr;gap:5px}
.action-grid span{height:44px;display:flex;align-items:center;justify-content:center;color:var(--white);font:800 19px "Montserrat",sans-serif;border-radius:2px}
.action-grid .blue{background:var(--blue)}
.action-grid .dark{background:var(--ink)}
.perks-left{left:28px;top:232px;width:140px}
.perks-right{left:175px;top:232px;width:160px}
.perks-left li,.perks-right li{margin-bottom:9px;font-size:14px}
.contact-card{left:50px;top:580px;width:262px;height:118px;border:1px solid #d8d8da;border-radius:10px;text-align:center;background:rgba(255,255,255,.5)}
.contact-pill{position:absolute;left:26px;top:-16px;width:210px;height:30px;background:var(--ink);border-radius:5px;color:var(--white);font:500 14px "Roboto",sans-serif;display:flex;align-items:center;justify-content:center;gap:8px}
.owner-name{margin-top:20px;font:700 22px "Montserrat",sans-serif;color:var(--blue)}
.owner-role{font:600 9px "Montserrat",sans-serif;letter-spacing:1px}
.owner-phone{font:700 31px "Montserrat",sans-serif;color:var(--ink);line-height:1.1}
.mini-icons{left:160px;top:702px;display:flex;gap:5px}
.mini-icons span{width:14px;height:14px;border-radius:50%;background:var(--ink)}
.contact-lines{left:0;top:722px;width:360px;text-align:center;font:600 15px "Montserrat",sans-serif;color:var(--ink);line-height:1.4}
.mailer{left:390px;top:36px;width:300px;height:724px;border:1.5px dashed #8a8a8e;border-radius:20px;overflow:hidden}
.mailer-fade{position:absolute;left:0;bottom:0;width:100%;height:260px;background:linear-gradient(180deg,rgba(255,255,255,0),rgba(205,205,208,.55))}
.return-address{position:absolute;left:186px;top:60px;transform-origin:0 0;transform:rotate(90deg);white-space:nowrap;font-size:13px;line-height:1.3;color:var(--ink)}
.return-address .brand{font-size:10px;gap:6px;margin-bottom:4px}
.cover-brand{left:760px;top:52px;width:290px;flex-direction:column;gap:12px;text-align:center}
.cover-hero{left:792px;top:276px;width:222px;height:256px;background:linear-gradient(180deg,#9fb3c6 0%,#d8cdbd 40%,#c07a3d 62%,#8c9a6c 100%)}
.script-1{left:740px;top:560px;width:320px;text-align:center;font:28px "Yellowtail",cursive;color:var(--white)}
.script-2{left:740px;top:590px;width:320px;text-align:center;font:38px "Yellowtail",cursive;color:var(--blue)}
.serving{left:740px;top:650px;width:320px;text-align:center;font:500 13.5px "Roboto",sans-serif;color:var(--white)}
.cover-headline{left:740px;top:674px;width:320px;text-align:center;font:800 30px/1 "Montserrat",sans-serif;color:var(--gold)}
/* inside */
.inside-title{left:0;top:28px;width:880px;height:68px;background:var(--ink);clip-path:polygon(0 0,100% 0,96% 100%,0 100%);color:var(--white);font:400 24px "Roboto",sans-serif;display:flex;align-items:center;padding-left:24px}
.inside-title b{font-weight:700;margin-left:6px}
.title-slash{left:872px;top:28px;width:48px;height:68px;background:var(--gold);clip-path:polygon(60% 0,100% 0,40% 100%,0 100%)}
.corner-brand{left:950px;top:36px;flex-direction:column;gap:4px;font-size:9px;text-align:center}
.body-copy{font-size:12px;line-height:1.38;text-align:justify}
.consult{left:24px;top:112px;width:312px}
.story{left:24px;top:682px;width:312px}
.service-head{width:254px;height:33px;display:flex;align-items:center;justify-content:center;color:var(--white);font:600 17px "Montserrat",sans-serif;letter-spacing:1.5px;border-radius:3px}
.service-head.blue{background:var(--blue)}
.service-head.dark{background:var(--ink)}
.service-head.gold{background:var(--gold);color:var(--ink)}
.services li{font-size:13.5px;margin-bottom:5px;padding-left:26px}
.mission-title{left:740px;top:594px;width:320px;display:flex;align-items:center;justify-content:center;gap:14px;font:36px "Yellowtail",cursive;color:var(--blue)}
.mission-title::before,.mission-title::after{content:"";width:44px;height:1.5px;background:var(--ink)}
.mission{left:756px;top:646px;width:300px;font-size:11px}
</style>
</head>
<body>

<div class="section-label" style="top:362px">BROCHURE OUTSIDE</div>

<section class="spread outside" style="top:410px" aria-label="Brochure outside spread">
  <svg class="spread-bg" viewBox="0 0 1080 838" aria-hidden="true">
    <polygon points="260,784 1080,322 1080,784" fill="#1f1f22"/>
    <polygon points="212,784 1080,296 1080,316 252,784" fill="#c9a66b"/>
    <rect x="782" y="266" width="242" height="276" fill="none" stroke="#c9a66b" stroke-width="12"/>
  </svg>

  <p class="intro">Whether you need a major repair, a renovation, or to check off a list of honey-dos, I can deliver professional skills at a fair price. It is our highest priority to get the job done right, the first time, on every assignment.</p>

  <div class="action-grid">
    <span class="blue">FIX IT</span><span class="dark">REPAIR IT</span>
    <span class="dark">CHANGE IT</span><span class="blue">BUILD IT</span>
  </div>

  <ul class="ticks perks-left">
    <li>35 years Experience</li>
    <li>Free Written Estimates</li>
    <li>Fully Insured</li>
    <li>Locally Owned</li>
  </ul>
  <ul class="ticks perks-right">
    <li>Prompt Response</li>
    <li>Trained Personnel</li>
    <li>Quality Materials</li>
    <li>References on Request</li>
  </ul>

  <div class="photo" role="img" aria-label="Photo of a freshly stained wooden deck floor" style="left:20px;top:408px;width:102px;height:142px;background:linear-gradient(180deg,#c9c4bb 0%,#a9653a 40%,#7a3f1f 100%)"></div>
  <div class="photo" role="img" aria-label="Photo of white deck railings and steps" style="left:128px;top:408px;width:102px;height:142px;background:linear-gradient(180deg,#6c7a52 0%,#dcdcd8 50%,#8d8a82 100%)"></div>
  <div class="photo" role="img" aria-label="Photo of new stair treads with white railings" style="left:236px;top:408px;width:102px;height:142px;background:linear-gradient(180deg,#d9d9d6 0%,#8b847a 55%,#5a524a 100%)"></div>

  <div class="contact-card">
    <div class="contact-pill">
      <svg width="12" height="18" viewBox="0 0 12 18" aria-hidden="true"><rect x="1" y="1" width="10" height="16" rx="2" fill="none" stroke="#fff" stroke-width="1.6"/><line x1="4.5" y1="14" x2="7.5" y2="14" stroke="#fff" stroke-width="1.4"/></svg>
      One Call Does IT ALL
    </div>
    <div class="owner-name">DALE MORROW</div>
    <div class="owner-role">OWNER</div>
    <div class="owner-phone">(207) 555-0148</div>
  </div>
  <div class="mini-icons" aria-hidden="true"><span></span><span></span></div>
  <div class="contact-lines">dale@twrhandyman.com<br>www.twrhandyman.com</div>

  <div class="mailer">
    <div class="mailer-fade" role="img" aria-label="Faded photo of a white porch railing"></div>
    <div class="return-address">
      <div class="brand"><span class="brand-square" style="width:16px;height:16px;border-width:2px"></span>TWR Handyman Services</div>
      TWR Handyman Services<br>120 B Mill Pond Rd<br>Seacrest, Maine 04099
    </div>
  </div>

  <div class="brand cover-brand">
    <span class="brand-square" style="width:86px;height:86px;border-width:7px"></span>
    TWR Handyman Services
  </div>
  <div class="cover-hero" role="img" aria-label="Photo of a new two-level stained wood deck on a gray house"></div>

  <div class="script-1">We are the solution</div>
  <div class="script-2">To Your Problems!</div>
  <div class="serving">Serving Southern Maine For All Your</div>
  <div class="cover-headline">PAINTING AND<br>REMODELING<br>NEEDS</div>

  <div class="bottom-bar">
    <div class="blue">Mail us : dale@twrhandyman.com</div>
    <div class="gold">Visit Us : www.twrhandyman.com</div>
    <div class="blue call">CALL US : (207) 555-0148</div>
  </div>
</section>

<div class="section-label" style="top:2240px">BROCHURE INSIDE</div>

<section class="spread inside" style="top:1388px" aria-label="Brochure inside spread">
  <div class="inside-title">Serving Southern Maine for All Your <b>Painting and Remodeling Needs</b></div>
  <div class="title-slash"></div>
  <div class="brand corner-brand"><span class="brand-square" style="width:40px;height:40px;border-width:3px"></span>TWR Handyman Services</div>

  <p class="body-copy consult">We provide a full consultation to explain available options so that you can choose the service that's right for your home or business. We strive to meet your project's needs and also to prevent potential problems in the future.</p>

  <div class="photo" role="img" aria-label="Photo of a room prepped for painting" style="left:22px;top:210px;width:154px;height:122px;background:linear-gradient(180deg,#e8e6e2,#b8b2a8)"></div>
  <div class="photo" role="img" aria-label="Photo of kitchen cabinets prepped for painting" style="left:180px;top:210px;width:156px;height:122px;background:linear-gradient(180deg,#dcdad6,#8e8a84)"></div>
  <div class="photo" role="img" aria-label="Photo of a living room with covered floor and ladder during renovation" style="left:22px;top:336px;width:314px;height:186px;background:linear-gradient(180deg,#e9ddc9 0%,#c8b89c 55%,#d9d6d0 100%)"></div>
  <div class="photo" role="img" aria-label="Photo of white kitchen cabinets being painted" style="left:22px;top:526px;width:154px;height:124px;background:linear-gradient(180deg,#d9d4cc,#6f6a64)"></div>
  <div class="photo" role="img" aria-label="Photo of finished dark painted kitchen cabinets" style="left:180px;top:526px;width:156px;height:124px;background:linear-gradient(180deg,#bdb9b3,#4a4c52)"></div>

  <p class="body-copy story">I have always been that person who can fix anything. Repair knowledge is not enough without skills. From woodworking to electrical installation, I have fostered all of the skills you need for household repairs and improvements.</p>

  <div class="service-head blue" style="left:410px;top:104px">INTERIOR PAINTING</div>
  <ul class="ticks services" style="left:412px;top:148px">
    <li>Commercial &amp; Residential</li><li>Kitchen Cabinets</li><li>Painting</li>
    <li>Walls trim &amp; doors</li><li>Celling repair</li><li>Staining &amp; polying trim</li>
  </ul>
  <div class="service-head dark" style="left:410px;top:286px">EXTERIOR PAINTING</div>
  <ul class="ticks services" style="left:412px;top:330px">
    <li>Commercial &amp; Residential</li><li>New Painting &amp; Updates</li><li>All types of Siding</li>
    <li>Power washing</li><li>Painting &amp; Staining of decks</li><li>Fence cleaning painting &amp; sealing</li>
    <li>Furniture cleaning, painting &amp; sealing</li>
  </ul>
  <div class="service-head gold" style="left:410px;top:492px">CARPENTRY</div>
  <ul class="ticks services" style="left:412px;top:536px;width:230px">
    <li>Commercial &amp; Residential</li><li>Kitchen remodeling</li><li>Marble &amp; Granite countertops</li>
    <li>Bathroom remodeling</li><li>Basement remodeling</li><li>Disabled accessible ramps &amp; bathroom ins installation</li>
    <li>Room additions</li><li>All types of siding</li><li>Cabinetry</li><li>Sheet rocking</li>
  </ul>

  <div class="service-head dark" style="left:770px;top:104px">MAINTENANCE</div>
  <ul class="ticks services" style="left:772px;top:148px">
    <li>Commercial &amp; Residential</li><li>Hanging Curtin's &amp; Blinds</li><li>Shelving</li>
    <li>Lighting</li><li>Picture hanging</li><li>TV mounting</li>
    <li>Desk &amp; furniture assembly</li><li>Fixture installation &amp; repair</li><li>Clean out basement &amp; storage areas</li>
  </ul>

  <div class="photo" role="img" aria-label="Photo of a stained cedar-sided cottage on a lawn" style="left:746px;top:362px;width:156px;height:204px;background:linear-gradient(180deg,#b8c8d8 0%,#b77a45 45%,#5f8a3a 100%)"></div>
  <div class="photo" role="img" aria-label="Photo of a new entry door with gray siding and steps" style="left:906px;top:362px;width:156px;height:204px;background:linear-gradient(180deg,#5c6c84 0%,#d6d8da 50%,#7a4a36 100%)"></div>

  <div class="mission-title">The Mission</div>
  <p class="body-copy mission">At TWR Handyman Services we are committed to client satisfaction and understanding that customer service is the foundation of our business. We are dedicated to providing our clients with quality workmanship performed in a prompt, professional manner. Our reliable team, second to non, will arrive neat in appearance and ready to work. Our technicians will treat each job, large or small, with the same care we would if we were repairing our own home.</p>

  <div class="bottom-bar">
    <div class="blue">Mail us : dale@twrhandyman.com</div>
    <div class="gold">Visit Us : www.twrhandyman.com</div>
    <div class="blue call">CALL US : (207) 555-0148</div>
  </div>
</section>

</body>
</html>
```